Harbor Dental, LLC business card project

Business card to be designed with current logo.
Dental office- please keep design of card that looks clean and professional.
Please include the following info:
Harbor Dental, LLC
Dr. Corinne Pelham
3187 Elmwood
Marlow Falls, PA 18342
610-392-7158
harbordental.office@quillmail.net
Updates
Hello everyone-
Project Deadline Extended
Reason: Just got back from overseas- will look at all designs and provide feedback. Thank you!
Project Deadline Extended
Reason: Polling my friends for the final selection-
thank you to all those that participated- so many talented designers!
Business

```html
<!DOCTYPE html>
<html lang="en">
<head>
<meta charset="utf-8">
<title>Harbor Dental, LLC – Business Card</title>
<link href="https://fonts.googleapis.com/css2?family=Mulish:wght@400;500&display=swap" rel="stylesheet">
<style>
  :root {
    --backdrop: #ececec;
    --card: #ffffff;
    --green: #5f9b2f;
    --skin-light: #f6dccd;
    --skin-mid: #e9b9a2;
    --skin-deep: #d99684;
  }
  * { box-sizing: border-box; margin: 0; padding: 0; }
  html, body {
    width: 1200px; height: 799px; overflow: hidden;
    background: var(--backdrop);
    font-family: "Mulish", "Helvetica Neue", Arial, sans-serif;
  }
  .business-card {
    position: absolute; left: 110px; top: 114px;
    width: 980px; height: 560px;
    background: var(--card);
    box-shadow: 0 10px 30px rgba(0,0,0,.12);
    overflow: hidden;
  }
  .smile-photo {
    position: absolute; right: 0; top: 0;
    width: 400px; height: 100%;
    background: radial-gradient(ellipse at 55% 50%, var(--skin-light) 0%, var(--skin-mid) 60%, var(--skin-deep) 100%);
  }
  .brand {
    position: absolute; left: 70px; top: 120px;
    display: flex; align-items: center; gap: 14px;
    color: var(--green);
  }
  .brand-dot {
    width: 22px; height: 22px; border-radius: 50%;
    background: var(--green);
  }
  .brand-name {
    font-size: 48px; font-weight: 400; letter-spacing: -0.5px;
  }
  .doctor-name {
    position: absolute; left: 70px; top: 250px;
    font-size: 36px; font-weight: 400; color: var(--green);
  }
  .contact {
    position: absolute; left: 70px; top: 340px;
    font-size: 24px; line-height: 1.35; color: var(--green);
    list-style: none;
  }
  .contact .gap { margin-top: 14px; }
</style>
</head>
<body>
  <article class="business-card">
    <div class="smile-photo" role="img" aria-label="Close-up photograph of a smiling mouth with white teeth"></div>

    <header class="brand">
      <span class="brand-dot"></span>
      <span class="brand-name">Harbor Dental, LLC</span>
    </header>

    <h1 class="doctor-name">Dr. Corinne Pelham</h1>

    <ul class="contact">
      <li>3187 Elmwood</li>
      <li>Marlow Falls, PA 18342</li>
      <li class="gap">P. 610.392.7158</li>
      <li>harbordental.office@quillmail.net</li>
    </ul>
  </article>
</body>
</html>
```